Property developer, money partner needs business card design using logo concept provided

Our company develops residential properties, does money lends for joint ventures in property deals and finds property deals for other money partners. We have provided a basic logo for you to work from. Any graphic or logo design on the card is to communicate development and finance collaboration. Color choice is not so important for us, but color choice does need to reflect professionalism.

```html
<!DOCTYPE html>
<html lang="en">
<head>
<meta charset="utf-8">
<title>Bridgeway Property Partners – Business Card</title>
<link href="https://fonts.googleapis.com/css2?family=Open+Sans:wght@400;600;700&display=swap" rel="stylesheet">
<style>
  :root{
    --stage:#2b2b2d;
    --card:#1d1d1f;
    --blue:#1257ab;
    --red:#a81e22;
    --white:#f2f2f2;
    --muted:#9a9a9a;
    --line:#cfcfcf;
  }
  *{box-sizing:border-box;margin:0;padding:0}
  html,body{width:1200px;height:780px;overflow:hidden}
  body{background:var(--stage);font-family:"Open Sans",Arial,sans-serif;position:relative}

  .card{position:absolute;top:235px;width:540px;height:309px;background:var(--card);overflow:hidden;
        box-shadow:0 14px 30px rgba(0,0,0,.45)}
  .card--front{left:40px}
  .card--back{left:620px}

  /* brand block */
  .brand{position:absolute;left:48px;top:70px;display:flex;align-items:center;gap:10px}
  .brand__dot{width:44px;height:44px;border-radius:50%;background:var(--blue)}
  .brand__text{color:var(--white);font-weight:600;line-height:1.25}
  .brand__name{font-size:15px;letter-spacing:2px;text-transform:uppercase}
  .brand__sub{font-size:9.5px;letter-spacing:.8px}
  .brand__reg{font-size:6.5px;letter-spacing:1px;color:var(--white)}

  .divider{position:absolute;left:238px;top:78px;width:1px;height:150px;background:var(--line);
           transform:rotate(28deg);opacity:.8}

  .person{position:absolute;left:300px;top:86px}
  .person__name{font-size:24px;font-weight:700;line-height:1.1}
  .person__first{color:var(--red)}
  .person__last{color:var(--blue)}
  .person__title{font-size:13px;color:var(--white);margin-top:3px}

  .contacts{list-style:none;margin-top:14px}
  .contacts li{display:flex;align-items:center;gap:8px;font-size:12.5px;color:var(--white);line-height:1.65}
  .contacts svg{width:12px;height:12px;flex:none}

  .address-band{position:absolute;left:0;bottom:22px;width:440px;height:34px;background:var(--blue);
                color:var(--white);font-size:13.5px;display:flex;align-items:center;padding-left:26px}
  .accent-red{position:absolute;right:0;bottom:22px;width:100px;height:34px;background:var(--red)}
  .band-dot{position:absolute;left:418px;bottom:16px;width:46px;height:46px;border-radius:50%;background:var(--blue);
            border:3px solid var(--card)}

  /* back */
  .back-pattern{position:absolute;inset:0;
     background:linear-gradient(100deg,#111 0%,#161616 55%,#3c3c3c 78%,#9a9a9a 100%)}
  .back-brand{position:absolute;left:50%;top:50%;transform:translate(-50%,-50%);display:flex;align-items:center;gap:6px}
  .back-brand__dot{width:16px;height:16px;border-radius:50%;background:var(--blue)}
  .back-brand__name{font-size:9px;font-weight:600;letter-spacing:1.5px;color:var(--white);text-transform:uppercase}
</style>
</head>
<body>

<section class="card card--front" aria-label="Business card front">
  <div class="brand">
    <span class="brand__dot"></span>
    <div class="brand__text">
      <div class="brand__name">Bridgeway</div>
      <div class="brand__sub">Property Partners</div>
      <div class="brand__reg">Reg No 104 220</div>
    </div>
  </div>

  <span class="divider"></span>

  <div class="person">
    <div class="person__name"><span class="person__first">Lena</span> <span class="person__last">Hartwell</span></div>
    <div class="person__title">Managing Director</div>
    <ul class="contacts">
      <li>
        <svg viewBox="0 0 24 24" aria-hidden="true"><path fill="var(--red)" d="M6.6 10.8a15.1 15.1 0 0 0 6.6 6.6l2.2-2.2a1 1 0 0 1 1-.25 11.4 11.4 0 0 0 3.6.57 1 1 0 0 1 1 1V20a1 1 0 0 1-1 1A17 17 0 0 1 3 4a1 1 0 0 1 1-1h3.5a1 1 0 0 1 1 1c0 1.25.2 2.45.57 3.57a1 1 0 0 1-.25 1z"/></svg>
        (555) 014-2287
      </li>
      <li>
        <svg viewBox="0 0 24 24" aria-hidden="true"><rect x="2" y="5" width="20" height="14" rx="2" fill="var(--red)"/><path d="M3 6l9 7 9-7" fill="none" stroke="var(--card)" stroke-width="2"/></svg>
        hello@bridgewaypp.com
      </li>
      <li>
        <svg viewBox="0 0 24 24" aria-hidden="true"><circle cx="12" cy="12" r="10" fill="var(--red)"/><path d="M2 12h20M12 2c3 3 3 17 0 20M12 2c-3 3-3 17 0 20" fill="none" stroke="var(--card)" stroke-width="1.5"/></svg>
        www.bridgewaypp.com
      </li>
    </ul>
  </div>

  <div class="accent-red"></div>
  <div class="address-band">1840 Elmcrest Ave. Suite 300 Denton, TX 76201</div>
  <span class="band-dot"></span>
</section>

<section class="card card--back" aria-label="Business card back">
  <div class="back-pattern" role="img" aria-label="Repeating brand-mark pattern fading from black to silver"></div>
  <div class="back-brand">
    <span class="back-brand__dot"></span>
    <span class="back-brand__name">Bridgeway</span>
  </div>
</section>

</body>
</html>
```